Letterhead Design Project

Attached is our new Logo and a copy of our old letter head
Looking to rebrand with our new logo

Reason: I want to show a business card design

Industry/Entity Type

Film Production

Colors

Designer to choose colors to be used in the design.

Requirements
Must have
• The information on the old letterhead

```html
<!DOCTYPE html>
<html lang="en">
<head>
<meta charset="utf-8">
<title>Varro International – Business Card</title>
<link rel="stylesheet" href="https://fonts.googleapis.com/css2?family=Open+Sans:wght@400;600;700&display=swap">
<style>
  :root {
    --backdrop: #4f9fd8;
    --blue-deep: #0a4a9e;
    --blue-mid: #1379c9;
    --blue-bright: #2ec4f0;
    --grey-band: #c4c6c8;
    --grey-light: #e4e5e6;
    --white: #ffffff;
    --ink: #555a60;
    --accent: #f07a1e;
  }
  * { margin: 0; padding: 0; box-sizing: border-box; }
  html, body { width: 1200px; height: 856px; overflow: hidden; }
  body {
    background: var(--backdrop);
    font-family: "Open Sans", Arial, sans-serif;
    display: flex;
    align-items: center;
    justify-content: center;
    gap: 40px;
  }
  .card {
    position: relative;
    width: 540px;
    height: 310px;
    border-radius: 22px;
    overflow: hidden;
    box-shadow: 0 14px 30px rgba(8, 40, 90, 0.35);
  }
  .card svg.card-art { position: absolute; inset: 0; }

  .brand {
    position: absolute;
    display: flex;
    align-items: center;
    gap: 8px;
    font-weight: 700;
    letter-spacing: 0.5px;
    white-space: nowrap;
  }
  .brand-dot { width: 13px; height: 13px; border-radius: 50%; }

  /* front */
  .card-front { background: var(--white); }
  .card-front .brand { left: 175px; top: 38px; font-size: 21px; color: var(--blue-mid); }
  .card-front .brand-dot { background: var(--accent); }
  .contact {
    position: absolute;
    left: 195px;
    top: 90px;
    list-style: none;
    font-size: 11.5px;
    color: var(--ink);
    line-height: 21px;
  }
  .contact li { display: flex; align-items: center; gap: 7px; white-space: nowrap; }
  .contact .sep { margin-left: 8px; }
  .icon { width: 11px; height: 11px; flex: none; }
  .holder {
    position: absolute;
    left: 30px;
    bottom: 30px;
    color: var(--white);
  }
  .holder-name { font-size: 20px; font-weight: 700; }
  .holder-role { font-size: 12px; letter-spacing: 1px; text-transform: uppercase; opacity: 0.9; }

  /* back */
  .card-back { background: var(--blue-deep); }
  .card-back .brand { right: 36px; top: 56px; font-size: 26px; color: var(--white); }
  .card-back .brand-dot { background: var(--white); }
  .web {
    position: absolute;
    left: 28px;
    bottom: 22px;
    font-size: 13px;
    font-weight: 600;
    color: var(--ink);
  }
</style>
</head>
<body>

  <section class="card card-front" aria-label="Business card front">
    <svg class="card-art" viewBox="0 0 540 310" aria-hidden="true">
      <defs>
        <linearGradient id="frontBlue" x1="0" y1="0" x2="0.6" y2="1">
          <stop offset="0" stop-color="#2ec4f0"/>
          <stop offset="0.5" stop-color="#1379c9"/>
          <stop offset="1" stop-color="#0a4a9e"/>
        </linearGradient>
        <linearGradient id="cornerBlue" x1="0" y1="0" x2="1" y2="1">
          <stop offset="0" stop-color="#0a4a9e"/>
          <stop offset="1" stop-color="#2ec4f0"/>
        </linearGradient>
      </defs>
      <path d="M340,0 L540,0 L540,120 C505,55 430,12 340,0 Z" fill="url(#cornerBlue)"/>
      <path d="M0,0 L100,0 C120,90 170,165 250,212 C150,150 60,105 0,50 Z" fill="var(--grey-band)"/>
      <path d="M0,62 C110,160 260,225 440,236 C400,250 370,280 355,310 L0,310 Z" fill="url(#frontBlue)"/>
    </svg>

    <div class="brand"><span class="brand-dot"></span>Varro International</div>

    <ul class="contact">
      <li><svg class="icon" viewBox="0 0 12 12"><circle cx="6" cy="6" r="6" fill="#f07a1e"/><circle cx="6" cy="5" r="2" fill="#fff"/></svg>P.O. Box 482 Lakeview QLD 4102</li>
      <li><svg class="icon" viewBox="0 0 12 12"><circle cx="6" cy="6" r="6" fill="#f07a1e"/><circle cx="6" cy="5" r="2" fill="#fff"/></svg>P.O. Box 317 Elmford NSW 2215
        <svg class="icon sep" viewBox="0 0 12 12"><circle cx="6" cy="6" r="6" fill="#f07a1e"/><rect x="3" y="4" width="6" height="4" fill="#fff"/></svg>hello@varro.com.au</li>
      <li><svg class="icon" viewBox="0 0 12 12"><circle cx="6" cy="6" r="6" fill="#f07a1e"/><rect x="3.5" y="3" width="5" height="6" rx="1" fill="#fff"/></svg>0400 118 225
        <svg class="icon sep" viewBox="0 0 12 12"><circle cx="6" cy="6" r="6" fill="#f07a1e"/></svg>ABN 51 204 618 735</li>
      <li><svg class="icon" viewBox="0 0 12 12"><circle cx="6" cy="6" r="6" fill="#f07a1e"/></svg>ACN 204 618 735</li>
    </ul>

    <div class="holder">
      <div class="holder-name">Example Name</div>
      <div class="holder-role">Designation</div>
    </div>
  </section>

  <section class="card card-back" aria-label="Business card back">
    <svg class="card-art" viewBox="0 0 540 310" aria-hidden="true">
      <defs>
        <linearGradient id="backBlue" x1="0" y1="0" x2="0.5" y2="1">
          <stop offset="0" stop-color="#2ec4f0"/>
          <stop offset="0.55" stop-color="#1379c9"/>
          <stop offset="1" stop-color="#0a4a9e"/>
        </linearGradient>
        <linearGradient id="backGrey" x1="0" y1="0" x2="1" y2="1">
          <stop offset="0" stop-color="#c4c6c8"/>
          <stop offset="1" stop-color="#e4e5e6"/>
        </linearGradient>
      </defs>
      <rect width="540" height="310" fill="url(#backBlue)"/>
      <path d="M0,20 C150,30 300,150 440,280 C300,200 150,90 0,60 Z" fill="#0a4a9e"/>
      <path d="M0,50 C160,80 310,190 470,290 C310,230 150,140 0,100 Z" fill="#2ec4f0" opacity="0.8"/>
      <path d="M0,70 C150,110 290,220 460,310 L0,310 Z" fill="url(#backGrey)"/>
    </svg>

    <div class="brand"><span class="brand-dot"></span>Varro International</div>
    <div class="web">www.varrointernational.com</div>
  </section>

</body>
</html>
```